Marwick Estate Services (Handyman / Home Improvement Company)

Looking for a double sided professional looking business card with Logo attached to be highlighted on one side and throwing in an image of a handyman as an option would be nice to see as well. We are a company focused on providing quality Handyman and Home improvement services in a timely manner that is done right the first time with integrity

Industry/Entity Type

Handyman / Home Improvement

Contact Information for Business Card

(LOGO, Name, Mobile and office phone numbers, email) on front side of card, (the words "The SOLUTION to all of your Handyman and Home Improvement needs" followed by "Family Owned and Operated" at the very bottom) on the back.

Colors
EB3D1F
EC4F4E
F09395
F8D3D4
FCEDEE

Requirements
Must have
• Red, Gray, Black Color scheme
Should not have
• No Yellow or Blue colors

```html
<!DOCTYPE html>
<html lang="en">
<head>
<meta charset="utf-8">
<title>Marwick Estate Services — Business Card</title>
<link rel="stylesheet" href="https://fonts.googleapis.com/css2?family=Lato:wght@400;700;900&display=swap">
<style>
  :root {
    --backdrop: #3b3e40;
    --card: #1d1d1e;
    --red: #e8202a;
    --white: #f2f2f2;
    --grey: #9a9a9a;
  }
  * { margin: 0; padding: 0; box-sizing: border-box; }
  html, body { width: 1200px; height: 1122px; overflow: hidden; }
  body {
    background: var(--backdrop);
    font-family: "Lato", sans-serif;
    position: relative;
  }
  .card {
    position: absolute;
    left: 150px;
    width: 900px;
    height: 500px;
    background: var(--card);
    border-radius: 28px;
    overflow: hidden;
  }
  .card--tagline { top: 41px; }
  .card--contact { top: 581px; }

  .brand-mark {
    display: flex;
    align-items: center;
    gap: 16px;
    font-weight: 900;
    color: var(--red);
    text-transform: uppercase;
    line-height: 1;
  }
  .brand-mark__dot {
    flex: none;
    border-radius: 50%;
    background: var(--grey);
  }

  .card--tagline .brand-mark {
    position: absolute;
    top: 130px;
    left: 0; right: 0;
    justify-content: center;
    font-size: 46px;
    letter-spacing: 1px;
  }
  .card--tagline .brand-mark__dot { width: 38px; height: 38px; }

  .tagline {
    position: absolute;
    top: 270px;
    left: 0; right: 0;
    text-align: center;
    color: var(--white);
    font-weight: 900;
    font-size: 30px;
    line-height: 1.22;
    text-transform: uppercase;
    letter-spacing: 0.5px;
  }
  .tagline__accent { color: var(--red); }
  .family-note {
    position: absolute;
    top: 360px;
    left: 0; right: 0;
    text-align: center;
    color: var(--red);
    font-size: 22px;
    font-weight: 400;
  }

  .card--contact .brand-mark {
    position: absolute;
    top: 110px;
    right: 70px;
    font-size: 30px;
    gap: 12px;
  }
  .card--contact .brand-mark__dot { width: 26px; height: 26px; background: var(--white); }

  .rule-white {
    position: absolute;
    left: 370px;
    right: 40px;
    top: 292px;
    height: 3px;
    background: var(--white);
  }
  .person { position: absolute; left: 115px; top: 220px; }
  .person__name {
    color: var(--red);
    font-weight: 900;
    font-size: 44px;
    letter-spacing: 1px;
    text-transform: uppercase;
    line-height: 1;
  }
  .person__title {
    color: var(--white);
    font-size: 26px;
    margin-top: 10px;
  }
  .rule-red {
    position: absolute;
    left: 115px;
    width: 255px;
    top: 340px;
    height: 4px;
    background: var(--red);
  }
  .contact-list {
    position: absolute;
    left: 115px;
    top: 362px;
    list-style: none;
    color: var(--white);
    font-size: 24px;
  }
  .contact-list li {
    display: flex;
    align-items: center;
    gap: 16px;
    height: 38px;
  }
  .contact-list svg { width: 22px; height: 22px; flex: none; }
</style>
</head>
<body>

<section class="card card--tagline">
  <div class="brand-mark"><span class="brand-mark__dot"></span>Marwick Estate Services</div>
  <p class="tagline">Your <span class="tagline__accent">Solution</span> to all of your<br>Handyman &amp; Home Improvement Needs</p>
  <p class="family-note">Family Owned &amp; Operated</p>
</section>

<section class="card card--contact">
  <div class="brand-mark"><span class="brand-mark__dot"></span>Marwick Estate Services</div>
  <div class="rule-white"></div>
  <div class="person">
    <h1 class="person__name">Daniel Rourke</h1>
    <p class="person__title">Founder &amp; CEO</p>
  </div>
  <div class="rule-red"></div>
  <ul class="contact-list">
    <li>
      <svg viewBox="0 0 24 24" aria-hidden="true"><path fill="#e8202a" d="M6.6 10.8a15 15 0 0 0 6.6 6.6l2.2-2.2a1 1 0 0 1 1-.25 11.4 11.4 0 0 0 3.6.57 1 1 0 0 1 1 1V20a1 1 0 0 1-1 1A17 17 0 0 1 3 4a1 1 0 0 1 1-1h3.5a1 1 0 0 1 1 1c0 1.25.2 2.45.57 3.6a1 1 0 0 1-.25 1z"/></svg>
      (555) 214-3870
    </li>
    <li>
      <svg viewBox="0 0 24 24" aria-hidden="true"><rect x="6" y="2" width="12" height="20" rx="2" fill="none" stroke="#e8202a" stroke-width="2"/><circle cx="12" cy="18" r="1.2" fill="#e8202a"/></svg>
      (555) 380-6142
    </li>
    <li>
      <svg viewBox="0 0 24 24" aria-hidden="true"><rect x="2" y="5" width="20" height="14" rx="1" fill="#e8202a"/><path d="M2 6l10 7 10-7" fill="none" stroke="#1d1d1e" stroke-width="1.6"/></svg>
      info@marwickestate.com
    </li>
  </ul>
</section>

</body>
</html>
```